étiquette 4.5 sur 12.5 cm pour shampooing pour chiens Morvelis

Étiquette pour six shampooings et un bain crème
produits destinés aux particuliers et distribués dans les animaleries;
retour à la formulation américaine initiale.
adaptable sur un flacon rond, partie visible de face cinq centimètres sur douze centimètres et demi de hauteur.
nous désirons une étiquette sur un fond de couleur pour pouvoir différencier visuellement et instantanément les différents produits.
le flacon est rond et de couleur blanche , l'étiquette recouvrira la presque totalité de ce flacon . l'étiquette totale est quatorze centimètres et 80milimètres

Target Market(s)

clients particuliers, produits distribués en animaleries

Font styles to use
Sans Serif

Requirements
Must have
• le nom MORVELIS en gras , puis PET CARE en plus petit
le type de produits ex: WHITE COAT SHAMPOO
l'explication du produit en 2 langues ex: shampooing chiens blancs
un dessin de chien
Nice to have
• un fond de couleur
un dessin de chien stylisé ou humoristique

```html
<!DOCTYPE html>
<html lang="fr">
<head>
<meta charset="utf-8">
<title>Morvelis Pet Care – shampoo labels</title>
<link rel="stylesheet" href="https://fonts.googleapis.com/css2?family=Montserrat:wght@800&family=Pathway+Gothic+One&display=swap">
<style>
  :root {
    --ink: #1a1a1a;
    --label-bg: #f4f5f7;
    --label-edge: #e2e4e8;
    --green-dark: #3dad6a;
    --green-light: #d9f0e2;
    --pink: #e0306f;
    --pink-light: #f6c5d6;
    --blue: #1fb5ea;
    --blue-light: #c4ebfa;
    --lime: #8cc63f;
    --lime-light: #e3f3c9;
    --coat-black: #2a2a2a;
    --coat-grey: #d7d8db;
  }
  * { box-sizing: border-box; margin: 0; padding: 0; }
  html, body {
    width: 1200px; height: 1000px; overflow: hidden;
    background: #ffffff;
  }
  .range {
    width: 1200px; height: 1000px;
    display: flex; justify-content: center; align-items: center;
    gap: 40px;
  }
  .label {
    width: 180px; height: 500px;
    background: linear-gradient(90deg, #e9ebee 0%, var(--label-bg) 18%, #fbfbfc 50%, var(--label-bg) 82%, #e9ebee 100%);
    border: 1px solid var(--label-edge);
    display: flex; flex-direction: column; align-items: center;
    padding-top: 22px;
  }
  .brand {
    font-family: "Montserrat", sans-serif;
    font-weight: 800; font-size: 21px; letter-spacing: 0.5px;
    color: var(--ink);
  }
  .line-band {
    width: 100%; height: 30px; margin-top: 8px;
    display: flex; align-items: center; justify-content: center;
    font-family: "Pathway Gothic One", sans-serif;
    font-size: 25px; color: var(--ink); letter-spacing: 0.5px;
  }
  .band-green { background: linear-gradient(90deg, var(--green-dark), var(--green-light) 35%, var(--green-light) 65%, var(--green-dark)); }
  .band-pink  { background: linear-gradient(90deg, var(--pink), var(--pink-light) 35%, var(--pink-light) 65%, var(--pink)); }
  .band-blue  { background: linear-gradient(90deg, var(--blue), var(--blue-light) 35%, var(--blue-light) 65%, var(--blue)); }
  .band-lime  { background: linear-gradient(90deg, var(--lime), var(--lime-light) 35%, var(--lime-light) 65%, var(--lime)); }

  .mascot {
    width: 156px; height: 272px; margin-top: 4px;
    border-radius: 44% 44% 40% 40%;
  }
  .mascot-black { background: radial-gradient(ellipse at 50% 55%, var(--coat-black) 0%, #555 45%, var(--coat-grey) 75%, #ffffff 100%); }
  .mascot-white { background: radial-gradient(ellipse at 50% 55%, #ffffff 0%, #f1f1f2 45%, var(--coat-grey) 80%, #ffffff 100%); }
  .mascot-pink  { background: radial-gradient(ellipse at 50% 55%, #ffffff 0%, #fbe3ec 40%, var(--pink) 78%, #f7d0dd 100%); }
  .mascot-blue  { background: radial-gradient(ellipse at 50% 55%, #ffffff 0%, #e2f5fd 40%, var(--blue) 78%, #c9edfb 100%); }
  .mascot-lime  { background: radial-gradient(ellipse at 50% 55%, #ffffff 0%, #eef8e0 40%, var(--lime) 78%, #dcf0c2 100%); }

  .product-name {
    margin-top: 16px;
    font-family: "Pathway Gothic One", sans-serif;
    font-size: 18px; letter-spacing: 0.3px;
  }
  .name-dark  { color: var(--ink); }
  .name-pink  { color: var(--pink); }
  .name-blue  { color: var(--blue); }
  .name-lime  { color: var(--lime); }

  .claims {
    list-style: none; margin-top: 6px; width: 138px;
    font-family: "Pathway Gothic One", sans-serif;
    font-size: 14px; line-height: 1.05; color: #333;
  }
  .claims li {
    position: relative; padding-left: 17px; margin-bottom: 4px;
  }
  .claims li::before {
    content: ""; position: absolute; left: 0; top: 2px;
    width: 9px; height: 9px; border-radius: 50%;
    background: var(--dot, var(--ink));
    border: 1.5px solid var(--dot, var(--ink));
  }
  .claims-hollow li::before { background: transparent; }
  .dot-pink { --dot: var(--pink); }
  .dot-blue { --dot: var(--blue); }
  .dot-lime { --dot: var(--lime); }
</style>
</head>
<body>
<main class="range">

  <article class="label">
    <div class="brand">MORVELIS</div>
    <div class="line-band band-green">PET CARE</div>
    <div class="mascot mascot-black" role="img" aria-label="Cartoon black dog with red collar in a cloud of white foam"></div>
    <h2 class="product-name name-dark">BLACK COAT SHAMPOO</h2>
    <ul class="claims">
      <li>shampooing chiens noir<br>un dessin de chien</li>
      <li>shampoo dogs black<br>a dog drawing</li>
    </ul>
  </article>

  <article class="label">
    <div class="brand">MORVELIS</div>
    <div class="line-band band-green">PET CARE</div>
    <div class="mascot mascot-white" role="img" aria-label="Cartoon white dog with red collar in a cloud of grey foam"></div>
    <h2 class="product-name name-dark">WHITE COAT SHAMPOO</h2>
    <ul class="claims claims-hollow">
      <li>shampooing chiens blanc<br>un dessin de chien</li>
      <li>shampoo dogs white<br>a dog drawing</li>
    </ul>
  </article>

  <article class="label">
    <div class="brand">MORVELIS</div>
    <div class="line-band band-pink">PET CARE</div>
    <div class="mascot mascot-pink" role="img" aria-label="Cartoon spotted dog with pink collar in a ring of pink foam bubbles"></div>
    <h2 class="product-name name-pink">SWEET SHAMPOO</h2>
    <ul class="claims dot-pink">
      <li>tous types de poils</li>
      <li>all types of hair</li>
    </ul>
  </article>

  <article class="label">
    <div class="brand">MORVELIS</div>
    <div class="line-band band-blue">PET CARE</div>
    <div class="mascot mascot-blue" role="img" aria-label="Cartoon spotted dog with blue collar in a ring of blue foam bubbles"></div>
    <h2 class="product-name name-blue">SENSITIV SHAMPOO</h2>
    <ul class="claims dot-blue">
      <li>soulage irritations<br>et démangeaisons</li>
      <li>relieves irritation<br>and itching</li>
    </ul>
  </article>

  <article class="label">
    <div class="brand">MORVELIS</div>
    <div class="line-band band-lime">PET CARE</div>
    <div class="mascot mascot-lime" role="img" aria-label="Cartoon spotted dog with green collar in a ring of green foam bubbles with green droplets"></div>
    <h2 class="product-name name-lime">REVITAL SHAMPOO</h2>
    <ul class="claims dot-lime">
      <li>régénérant et démêlant</li>
      <li>regenerating and detangling</li>
    </ul>
  </article>

</main>
</body>
</html>
```